Design an Exhibition Poster for our Web Application

Our company develops and sells VaultLarkly, a web-based service that helps small businesses to test their web applications for security vulnerabilities.

You can see details of the service at the following page:

https://www.vaultlarkly.example/

We need a poster designed, to be used on an exhibition stand at a professional security conference.
Updates

Project Deadline Extended
Reason: The deadline for this project is being extended because we have, so far, received very few design submissions and they are generally not of the aesthetic quality we are looking for.

Target Market(s)

Tech startups and small / medium sized online businesses

Industry/Entity Type

Security

Requirements
Must have
• [1] Incorporate the VaultLarkly logo (see attached file).

[2] Use the text supplied by us (see attached file).

[3] Use a color scheme that matches the scheme used on our website.

[4] Project the visual theme of cyber security (or protection against cyber crime).
Nice to have
• This is part of a 2-poster set. The project for designing the other poster in the set is also being listed on ArtFolio today. Please look for the project entitled "Design an Exhibition Poster for our Software Product".

Preference will be given to designers who submit a pair of designs that harmonize with each other.

```html
<!DOCTYPE html>
<html lang="en">
<head>
<meta charset="utf-8">
<title>VaultLarkly – Security For Web Startups</title>
<link rel="stylesheet" href="https://fonts.googleapis.com/css2?family=Open+Sans:wght@400;600;700&display=swap">
<style>
  :root {
    --paper: #ffffff;
    --brand-green: #7d9e3e;
    --band-light: #b6ca8f;
    --band-dark: #8ea852;
    --logo-grey: #7b7b7b;
    --ink-strong: #4a4a4a;
    --ink-list: #2b2b2b;
    --cta-text: #ffffff;
  }
  html, body {
    margin: 0;
    padding: 0;
    overflow: hidden;
    background: var(--paper);
  }
  .poster {
    position: relative;
    width: 848px;
    height: 1200px;
    overflow: hidden;
    background: var(--paper);
    font-family: "Open Sans", Arial, sans-serif;
  }
  .poster__bands {
    position: absolute;
    inset: 0;
    width: 848px;
    height: 1200px;
  }
  .band--light { fill: var(--band-light); }
  .band--dark { fill: var(--band-dark); }

  .brand {
    position: absolute;
    left: 86px;
    top: 78px;
    display: flex;
    align-items: center;
    gap: 28px;
  }
  .brand__mark {
    width: 96px;
    height: 96px;
    background: var(--brand-green);
  }
  .brand__name {
    margin: 0;
    font-size: 78px;
    font-weight: 600;
    color: var(--logo-grey);
    letter-spacing: 0.5px;
    line-height: 1;
  }
  .headline {
    position: absolute;
    left: 0;
    right: 0;
    top: 232px;
    margin: 0;
    text-align: center;
    padding-left: 50px;
    font-size: 46px;
    font-weight: 700;
    color: var(--brand-green);
    line-height: 1.1;
  }
  .intro {
    position: absolute;
    left: 54px;
    top: 308px;
    width: 760px;
    margin: 0;
    font-size: 29px;
    font-weight: 700;
    color: var(--ink-strong);
    line-height: 40px;
  }
  .benefits {
    position: absolute;
    left: 280px;
    top: 632px;
    margin: 0;
    padding: 0;
    list-style: none;
  }
  .benefits__item {
    display: flex;
    align-items: center;
    font-size: 49px;
    font-weight: 400;
    color: var(--ink-list);
    line-height: 64px;
  }
  .benefits__item::before {
    content: "";
    width: 15px;
    height: 15px;
    margin-right: 24px;
    background: var(--ink-list);
    transform: rotate(45deg);
  }
  .cta {
    position: absolute;
    right: 50px;
    top: 1110px;
    margin: 0;
    font-size: 29px;
    font-weight: 700;
    color: var(--cta-text);
  }
</style>
</head>
<body>
  <main class="poster">
    <svg class="poster__bands" viewBox="0 0 848 1200" aria-hidden="true">
      <polygon class="band--light" points="0,630 848,336 848,1200 0,1200"/>
      <polygon class="band--dark" points="0,1086 848,792 848,1200 0,1200"/>
    </svg>

    <header class="brand">
      <div class="brand__mark"></div>
      <p class="brand__name">VaultLarkly</p>
    </header>

    <h1 class="headline">Security For Web Startups</h1>
    <p class="intro">Online website vulnerability scanning that tells you exactly what needs fixing and<br>how to to fix it.</p>

    <ul class="benefits">
      <li class="benefits__item">Accessible</li>
      <li class="benefits__item">Affordable</li>
      <li class="benefits__item">Simple</li>
    </ul>

    <p class="cta">Try it Free Today!</p>
  </main>
</body>
</html>
```